Tidemoor Charters website

Looking to have a new, interactive website built on Wordpress and hosted by hostbrivo. Our current site was made and is hosted by plem and has been up and running for 8 years. Would like to replace as seamlessly as possible. Attached are general ideas for the site as well as requirements. Would like to showcase our charter options and information on the home page with Our Charters, FAQ and Gallery as follow up pages. Would like to be created in Wordpress and HTTPS

Target Market(s)

Vacationing tourists visiting Siesta Key

Industry/Entity Type

Boat Charters

Number of Pages Required

1 page

Requirements
Must have
• Website must be secure, HTTPS not HTTP . . Use webp images throughout the entire site. Info for the home page was uploaded on 3 seperate pages labeled home1, home2 and home3. Need the bottom, above footer, to show What Our Customers Say About Us with reviews from Wandermark, Zentra and QP. Homepage to have all 6 charter options and info provided on the attached docx labeled home1, home2 and home3 . If we can get the 3 pages following the home page (Our Charters,FAQ and Gallery) I had also attached brief summaries for those pages. Install these Plug-ins, YOST, Fareharbor (free), Elementor plugin. Any other plugin needs to be approved by us

```html
<!DOCTYPE html>
<html lang="en">
<head>
<meta charset="utf-8">
<title>Tidemoor Charters – Private Boat Tours on Siesta Key</title>
<link href="https://fonts.googleapis.com/css2?family=Montserrat:wght@600;700&family=Roboto:wght@400;500;700&display=swap" rel="stylesheet">
<style>
:root{
  --blue:#1769b3;
  --blue-deep:#0a67ad;
  --blue-title:#1a6db5;
  --orange:#f7941d;
  --sky-soft:#e3f4fc;
  --ink:#222;
  --ink-soft:#444;
  --night:#151515;
  --white:#fff;
}
*{box-sizing:border-box;margin:0;padding:0}
html,body{width:1200px;height:3625px;overflow:hidden;background:var(--white)}
body{font-family:"Roboto",Arial,sans-serif;color:var(--ink);position:relative}
.page{position:relative;width:1200px;height:3625px;overflow:hidden}
.abs{position:absolute}
.btn{position:absolute;display:flex;align-items:center;justify-content:center;gap:8px;font:700 13px "Roboto",sans-serif;text-transform:uppercase;letter-spacing:.2px}
.btn .dot{width:12px;height:12px;border-radius:50%;display:inline-flex;align-items:center;justify-content:center}
.btn .dot svg{width:8px;height:8px}

/* header */
.topline{right:162px;top:10px;font-size:13px;color:var(--ink);display:flex;align-items:center;gap:8px}
.topline .num{color:var(--orange);font-weight:700;font-size:19px;font-family:"Montserrat",sans-serif}
.navbar{left:459px;top:44px;width:741px;height:49px;background:var(--blue);border-radius:25px 0 0 25px;display:flex;align-items:center}
.navbar a{color:var(--white);text-decoration:none;font-size:14px;height:49px;display:flex;align-items:center;padding:0 17px}
.navbar a.current{background:var(--orange);margin-left:38px}
.navbar a.quote{background:var(--orange);font-weight:700;margin-left:18px;padding:0 23px;font-size:13px}
.brand{left:120px;top:-12px;width:192px;height:180px;border-radius:50%;background:var(--white);display:flex;align-items:center;justify-content:center;text-align:center;z-index:5;box-shadow:0 2px 6px rgba(0,0,0,.08)}
.brand span{font:700 21px/1.15 "Montserrat",sans-serif;color:var(--blue);margin-top:20px}

/* hero */
.hero{left:0;top:93px;width:1200px;height:561px;background:linear-gradient(100deg,#b8c9d3 0%,#7d8f86 18%,#caa48a 32%,#9fb2c2 50%,#5d7f9c 70%,#6f8ca6 100%)}
.hero-title{left:633px;top:258px;font:700 50px/1.2 "Montserrat",sans-serif;color:var(--white);width:560px}
.btn.start{left:635px;top:383px;width:142px;height:39px;background:var(--white);color:var(--blue)}
.btn.start .dot{background:var(--blue)}
.slide-arrow{top:490px;width:42px;height:42px;border-radius:50%;background:var(--white);display:flex;align-items:center;justify-content:center}

/* charters */
.charter{width:248px;height:248px;border-radius:50%}
.charter-label{width:300px;text-align:center;font-weight:700;font-size:17px;color:var(--ink)}
.sunset-band{left:0;top:1240px;width:1200px;height:277px;background:linear-gradient(180deg,rgba(255,255,255,1) 0%,#fde8d2 35%,#f8b774 58%,#f4913f 63%,#3f5b79 67%,#2b4867 100%)}

/* book */
.book{left:0;top:1517px;width:1200px;height:519px;background:var(--blue-deep)}
.book-photo{left:0;top:1517px;width:680px;height:519px;background:linear-gradient(90deg,#8fa0a8 0%,#c8b7a3 35%,#d7c8b5 60%,rgba(10,103,173,0) 100%)}
.book-title{left:590px;top:1598px;font:700 42px/1.15 "Montserrat",sans-serif;color:var(--white)}
.book-text{left:590px;font:400 15.5px/24px "Montserrat",sans-serif;color:var(--white);width:520px}
.btn.schedule{left:590px;top:1891px;width:183px;height:41px;background:var(--white);color:var(--blue)}
.btn.schedule .dot{background:var(--blue)}

/* about */
.about{left:0;top:2036px;width:1200px;height:621px;background:var(--sky-soft)}
.eyebrow{left:145px;top:2142px;font:700 15px "Montserrat",sans-serif;color:var(--ink)}
.about-title{left:145px;top:2166px;font:700 45px "Montserrat",sans-serif;color:var(--blue)}
.about-text{left:145px;top:2272px;width:434px;font-size:14.6px;line-height:24px;color:var(--ink-soft);text-align:justify}
.btn.more{left:145px;top:2507px;width:143px;height:41px;background:var(--blue);color:var(--white)}
.btn.more .dot{background:var(--white)}

/* reviews */
.reviews-title{left:0;top:2728px;width:1200px;text-align:center;font:700 33px "Montserrat",sans-serif;color:var(--blue-title)}
.review{top:2831px;width:280px;height:283px;background:var(--white);box-shadow:0 2px 12px rgba(0,0,0,.08);padding:26px 28px}
.review .who{display:flex;align-items:center;gap:12px}
.review .avatar{width:55px;height:55px;border-radius:50%;color:var(--white);font-size:22px;font-weight:500;display:flex;align-items:center;justify-content:center}
.review .name{font-weight:500;font-size:16.5px}
.review .when{font-size:13.5px;color:#555;margin-top:2px}
.review p{margin-top:22px;font-size:15.5px;line-height:24px;color:var(--ink-soft)}
.review .foot{position:absolute;left:28px;right:28px;bottom:34px;display:flex;justify-content:space-between;align-items:center}
.stars{color:#f5c000;font-size:17px;letter-spacing:2px}
.source{display:flex;align-items:center;gap:6px;font-size:13px;font-weight:500;color:var(--ink)}
.source i{width:14px;height:14px;border-radius:50%;display:inline-block}
.rev-arrow{top:2958px}

/* footer */
.foot-brand{left:149px;top:3388px;width:276px;height:136px;border-radius:50%;background:var(--white);display:flex;align-items:center;justify-content:center}
.foot-brand span{font:700 21px/1.15 "Montserrat",sans-serif;color:var(--blue);text-align:center}
.foot-nav{left:485px;top:3402px;display:flex;gap:20px;color:var(--white);font-size:15px;font-weight:500}
.foot-nav b{font-weight:400}
.contact{display:flex;align-items:center;gap:14px;color:var(--white);font-size:15px;line-height:24px;font-weight:500}
.contact .ic{width:46px;height:46px;border-radius:50%;background:var(--blue);display:flex;align-items:center;justify-content:center}
.rule{left:145px;top:3542px;width:912px;height:1px;background:#555}
.social{top:3564px;width:34px;height:34px;border-radius:50%;background:#2a2a2a;color:var(--white);font-size:10px;font-weight:700;display:flex;align-items:center;justify-content:center}
.social.on{background:var(--blue)}
.copy{right:143px;top:3570px;color:var(--white);font-size:15px}
</style>
</head>
<body>
<div class="page">

  <!-- header -->
  <div class="abs brand"><span>Tidemoor<br>Charters</span></div>
  <div class="abs topline">
    <svg width="13" height="13" viewBox="0 0 24 24"><path fill="#f7941d" d="M6.6 10.8a15 15 0 006.6 6.6l2.2-2.2c.3-.3.7-.4 1-.2 1.1.4 2.3.6 3.6.6.6 0 1 .4 1 1V20c0 .6-.4 1-1 1A17 17 0 013 4c0-.6.4-1 1-1h3.5c.6 0 1 .4 1 1 0 1.3.2 2.5.6 3.6.1.3 0 .7-.2 1z"/></svg>
    Call or Click for a Free Estimate <span class="num">941-555-0187</span>
  </div>
  <nav class="abs navbar">
    <a class="current">Home</a><a>Our Charters</a><a>FAQs</a><a>Gallery</a><a>Contact</a><a class="quote">GET A QUOTE</a>
  </nav>

  <!-- hero -->
  <section class="abs hero" role="img" aria-label="Friends relaxing on the bow of a sailboat on a mountain-ringed bay"></section>
  <svg class="abs" style="left:0;top:480px" width="1200" height="180" viewBox="0 0 1200 180">
    <path fill="#fff" d="M0,171 C200,160 350,82 490,86 C610,90 620,145 730,135 C900,118 1060,50 1200,58 L1200,180 L0,180 Z"/>
  </svg>
  <h1 class="abs hero-title">Best Private Boat Tour on Siesta Beach</h1>
  <div class="btn start">Get Started <span class="dot"><svg viewBox="0 0 8 8"><path d="M2.5 1.5L5 4 2.5 6.5" stroke="#fff" stroke-width="1.5" fill="none"/></svg></span></div>
  <div class="abs slide-arrow" style="left:554px"><svg width="12" height="12" viewBox="0 0 12 12"><path d="M8 2L4 6l4 4" stroke="#222" stroke-width="1.6" fill="none"/></svg></div>
  <div class="abs slide-arrow" style="left:602px"><svg width="12" height="12" viewBox="0 0 12 12"><path d="M4 2l4 4-4 4" stroke="#222" stroke-width="1.6" fill="none"/></svg></div>

  <!-- charters -->
  <div class="abs sunset-band" role="img" aria-label="Sun setting over the Gulf horizon"></div>
  <div class="abs charter" style="left:143px;top:719px;background:radial-gradient(circle at 55% 55%,#36586c,#5b89a8 55%,#c4d6e2)" role="img" aria-label="Dolphin leaping from the boat wake"></div>
  <div class="abs charter" style="left:475px;top:719px;background:radial-gradient(circle at 50% 60%,#6b6f6a,#a9c9c2 55%,#d7e6ea)" role="img" aria-label="Family posing on a sandbar"></div>
  <div class="abs charter" style="left:807px;top:719px;background:linear-gradient(180deg,#2f6cc0 0%,#7fa6d6 40%,#dde3ea 55%,#3a5972 80%,#22384c)" role="img" aria-label="Charter boat anchored near the shore"></div>
  <div class="abs charter" style="left:143px;top:1023px;background:linear-gradient(180deg,#5a8ed0 0%,#a9c6e6 50%,#2f7ba6 65%,#1e5d86)" role="img" aria-label="Sailboat moored off a beach"></div>
  <div class="abs charter" style="left:475px;top:1023px;background:radial-gradient(circle at 45% 45%,#d9b48e,#8a5a3a 60%,#3a2418)" role="img" aria-label="Friends toasting at a tiki bar"></div>
  <div class="abs charter" style="left:807px;top:1023px;background:linear-gradient(180deg,#e48a6e 0%,#f2a07c 40%,#8b7e86 60%,#4c5262)" role="img" aria-label="Sunset cruise on calm water"></div>
  <div class="abs charter-label" style="left:117px;top:982px">Dolphin/Wildlife Tours</div>
  <div class="abs charter-label" style="left:449px;top:982px">Sandbar Fun</div>
  <div class="abs charter-label" style="left:781px;top:982px">Snorkeling</div>
  <div class="abs charter-label" style="left:117px;top:1286px">Shelling &amp; Beaches</div>
  <div class="abs charter-label" style="left:449px;top:1286px">Tiki Bar Crawl</div>
  <div class="abs charter-label" style="left:781px;top:1286px">Sunset Cruise</div>

  <!-- book -->
  <section class="abs book"></section>
  <div class="abs book-photo" role="img" aria-label="Group of friends on a boat under a bridge by the beach"></div>
  <h2 class="abs book-title">Book Your Siesta Key<br>Boat Charter</h2>
  <svg class="abs" style="left:590px;top:1714px" width="96" height="14" viewBox="0 0 96 14"><path d="M2 7 Q10 1 18 7 T34 7 T50 7 T66 7 T82 7 T94 5" stroke="#fff" stroke-width="3" fill="none" stroke-linecap="round"/></svg>
  <p class="abs book-text" style="top:1740px">Dolphin Tours, Snorkeling, Sandbars, Tiki Bars,<br>Shelling, Sunsets</p>
  <p class="abs book-text" style="top:1813px">Design your day on the water. Customize your day your way!<br>Call or Email to coordinate and get help with suggestions.</p>
  <div class="btn schedule">Schedule Today <span class="dot"><svg viewBox="0 0 8 8"><path d="M2.5 1.5L5 4 2.5 6.5" stroke="#fff" stroke-width="1.5" fill="none"/></svg></span></div>

  <!-- about -->
  <section class="abs about"></section>
  <div class="abs eyebrow">ABOUT US</div>
  <h2 class="abs about-title">Tidemoor Charters</h2>
  <svg class="abs" style="left:145px;top:2240px" width="96" height="14" viewBox="0 0 96 14"><path d="M2 7 Q10 1 18 7 T34 7 T50 7 T66 7 T82 7 T94 5" stroke="#1769b3" stroke-width="3" fill="none" stroke-linecap="round"/></svg>
  <p class="abs about-text">Welcome to the BEST private charter on and around Siesta Key! Whether you live on Siesta Key, Sarasota or are one of our many welcome visitors… we want you to enjoy the day on the crystal clear waters and pristine beaches. My name is Dale Varen and I look forward to being your Captain for the day. My goal is to ensure a safe and fun time on the water. I will work hard to create unforgettable memories with a charter that you, your family and friends will remember. I have been boating since the age of 13 and am a USCG licensed Master Captain.</p>
  <div class="btn more">Read More <span class="dot"><svg viewBox="0 0 8 8"><path d="M2.5 1.5L5 4 2.5 6.5" stroke="#1769b3" stroke-width="1.5" fill="none"/></svg></span></div>
  <svg class="abs" style="left:621px;top:2123px" width="440" height="440" viewBox="0 0 440 440">
    <circle cx="220" cy="220" r="212" fill="none" stroke="#1769b3" stroke-width="3" stroke-dasharray="8 6" stroke-linecap="round"/>
    <circle cx="220" cy="220" r="204" fill="#fff"/>
  </svg>
  <div class="abs" style="left:637px;top:2139px;width:408px;height:408px;border-radius:50%;background:radial-gradient(circle at 55% 45%,#c9c3b8,#e4e1da 50%,#a9b3b8)" role="img" aria-label="Captain and family on the beach"></div>

  <!-- reviews -->
  <h2 class="abs reviews-title">What Our Charter Guests Have to Say About Us</h2>
  <svg class="abs" style="left:552px;top:2782px" width="96" height="14" viewBox="0 0 96 14"><path d="M2 7 Q10 1 18 7 T34 7 T50 7 T66 7 T82 7 T94 5" stroke="#1769b3" stroke-width="3" fill="none" stroke-linecap="round"/></svg>
  <svg class="abs rev-arrow" style="left:62px" width="24" height="28" viewBox="0 0 24 28"><path d="M16 3L6 14l10 11" stroke="#222" stroke-width="2.4" fill="none"/></svg>
  <svg class="abs rev-arrow" style="left:1115px" width="24" height="28" viewBox="0 0 24 28"><path d="M8 3l10 11-10 11" stroke="#222" stroke-width="2.4" fill="none"/></svg>

  <article class="abs review" style="left:145px">
    <div class="who"><div class="avatar" style="background:#f28c00">D</div><div><div class="name">Dana Tolliver</div><div class="when">10days ago</div></div></div>
    <p>Lorem ipsum dolor sit amet, consectetur adipiscing elit, sed do eiusmod tempor incididunt ut Ut enim ad minim veniam dolore magna aliqua.</p>
    <div class="foot"><span class="stars">★★★★★</span><span class="source"><i style="background:#34e0a1"></i>Wandermark</span></div>
  </article>
  <article class="abs review" style="left:460px">
    <div class="who"><div class="avatar" style="background:#2a6e8c">M</div><div><div class="name">Marla Fenwick</div><div class="when">10days ago</div></div></div>
    <p>Lorem ipsum dolor sit amet, consectetur adipiscing elit, sed do eiusmod tempor incididunt ut Ut enim ad minim veniam dolore magna aliqua.</p>
    <div class="foot"><span class="stars">★★★★★</span><span class="source"><i style="background:#e0453a"></i>Zentra</span></div>
  </article>
  <article class="abs review" style="left:777px">
    <div class="who"><div class="avatar" style="background:#53b948">J</div><div><div class="name">Jamie R</div><div class="when">10days ago</div></div></div>
    <p>Lorem ipsum dolor sit amet, consectetur adipiscing elit, sed do eiusmod tempor incididunt ut Ut enim ad minim veniam dolore magna aliqua.</p>
    <div class="foot"><span class="stars">★★★★★</span><span class="source"><i style="background:#1877f2"></i>QP</span></div>
  </article>

  <!-- footer -->
  <svg class="abs" style="left:0;top:3180px" width="1200" height="445" viewBox="0 0 1200 445">
    <path fill="#151515" d="M0,122 C150,150 300,150 450,130 C650,100 750,20 900,18 C1050,16 1120,40 1200,30 L1200,445 L0,445 Z"/>
  </svg>
  <div class="abs foot-brand"><span>Tidemoor<br>Charters</span></div>
  <div class="abs foot-nav"><span>Home</span><b>/</b><span>Our Charters</span><b>/</b><span>FAQS</span><b>/</b><span>Gallery</span><b>/</b><span>Contact</span></div>
  <div class="abs contact" style="left:484px;top:3463px">
    <span class="ic"><svg width="16" height="18" viewBox="0 0 24 24"><path fill="#fff" d="M12 2a7 7 0 00-7 7c0 5 7 13 7 13s7-8 7-13a7 7 0 00-7-7zm0 9.5A2.5 2.5 0 1112 6.5a2.5 2.5 0 010 5z"/></svg></span>
    <span>4120 Harborlight<br>Rd, Siesta Key</span>
  </div>
  <div class="abs contact" style="left:748px;top:3463px">
    <span class="ic"><svg width="16" height="16" viewBox="0 0 24 24"><path fill="#fff" d="M6.6 10.8a15 15 0 006.6 6.6l2.2-2.2c.3-.3.7-.4 1-.2 1.1.4 2.3.6 3.6.6.6 0 1 .4 1 1V20c0 .6-.4 1-1 1A17 17 0 013 4c0-.6.4-1 1-1h3.5c.6 0 1 .4 1 1 0 1.3.2 2.5.6 3.6.1.3 0 .7-.2 1z"/></svg></span>
    <span>Call or Click for a Free Estimate<br>941-555-0187</span>
  </div>
  <div class="abs rule"></div>
  <div class="abs social" style="left:145px">QP</div>
  <div class="abs social on" style="left:187px">Pix</div>
  <div class="abs social" style="left:228px">Vid</div>
  <div class="abs copy">© Copyrights 2024 | All Rights Reserved</div>

</div>
</body>
</html>
```